Harbrook Builders PowerPoint Presentation

We need a sales pitch in powerpoint form for a "commercial only" construction company based out of Dallas, TX. We perform commercial only construction including ground up, build to suit, white box and many others. We would like the design to match the color scheme and outlook of the website and brochure that will be attached. Also, attached you will find the old presentation we used (it's terrible). http://www.harbrookbld.example/

Target Market(s)

Commercial property managers, commercial building owners, business owners, facility managers, commercial construction managers, construction design teams

Industry/Entity Type

Construction

Requirements
Must have
• Commercial construction pictures. Company overview. Specific industries served.
Should not have
• Residential pictures. Poor quality pictures. Anything that doesn't look like the website or attached brochure.

```html
<!DOCTYPE html>
<html lang="en">
<head>
<meta charset="utf-8">
<title>Harbrook Builders – Presentation Slides</title>
<link rel="stylesheet" href="https://fonts.googleapis.com/css2?family=Montserrat:wght@400;500;600;700;800&display=swap">
<style>
  :root {
    --orange: #b4692b;
    --orange-bright: #f07a3a;
    --ink: #333333;
    --body: #555555;
    --footer: #4d5e5e;
    --rule: #9a9a9a;
    --grey-dot: #a8a8a8;
    --white: #ffffff;
    --page: #ffffff;
  }
  * { box-sizing: border-box; margin: 0; padding: 0; }
  html, body { width: 1200px; height: 1048px; overflow: hidden; background: var(--page); }
  body { position: relative; font-family: "Montserrat", Arial, sans-serif; color: var(--ink); }

  .slide { position: absolute; width: 574px; height: 324px; overflow: hidden; background: var(--white); box-shadow: 0 0 0 1px #f0f0f0; }
  .slide--one-col  { left: 20px;  top: 22px; }
  .slide--three-col{ left: 608px; top: 22px; }
  .slide--graphics { left: 20px;  top: 364px; }
  .slide--section  { left: 608px; top: 364px; background: var(--orange); box-shadow: none; }
  .slide--project  { left: 18px;  top: 706px; background: var(--orange); box-shadow: none; }
  .slide--stats    { left: 602px; top: 706px; }

  .top-rule { position: absolute; left: 20px; top: 0; width: 216px; height: 3px; background: var(--rule); }
  .top-rule--accent { background: var(--orange); }

  .slide-title { position: absolute; left: 20px; top: 15px; font-size: 21px; font-weight: 800; color: var(--ink); letter-spacing: -0.2px; }
  .slide-title span { color: var(--orange); }

  .brand { position: absolute; right: 12px; top: 10px; display: flex; align-items: center; gap: 4px; }
  .brand__dot { width: 11px; height: 11px; border-radius: 50%; background: var(--orange); }
  .brand__name { font-size: 13px; font-weight: 700; color: var(--ink); letter-spacing: 0.2px; }

  .footer { position: absolute; left: 0; bottom: 0; width: 100%; height: 12px; background: var(--footer); color: var(--white); font-size: 7px; line-height: 12px; padding-left: 6px; }

  .dot { position: absolute; border-radius: 50%; }
  .dot--orange { background: var(--orange); }
  .dot--grey { background: var(--grey-dot); }

  .photo { position: absolute; border-radius: 50%; }

  /* One column */
  .col-title { position: absolute; left: 27px; top: 66px; font-size: 14px; font-weight: 700; color: var(--orange); }
  .col-body { position: absolute; left: 28px; top: 84px; width: 228px; font-size: 7.6px; line-height: 13.7px; color: var(--body); text-align: justify; }
  .col-body p + p { margin-top: 14px; }
  .frame-ring { position: absolute; left: 311px; top: 81px; width: 198px; height: 198px; border-radius: 50%; border: 1px solid #b9b9b9; }
  .photo--workers { left: 316px; top: 86px; width: 188px; height: 188px; background: radial-gradient(circle at 45% 40%, #d8c79a 0%, #8c8a62 45%, #5b6a4a 100%); }

  /* Three columns */
  .feature { position: absolute; top: 81px; width: 160px; text-align: center; }
  .feature--a { left: 33px; } .feature--b { left: 202px; } .feature--c { left: 374px; }
  .photo--engineer { position: relative; left: 20px; top: 0; width: 120px; height: 120px; background: linear-gradient(160deg, #8fb3d8 0%, #6f86a1 40%, #b5c23f 70%, #5c5a52 100%); display: block; }
  .feature__title { margin-top: 14px; font-size: 13.5px; font-weight: 700; color: var(--orange); }
  .feature__body { margin-top: 2px; font-size: 7.6px; line-height: 13.7px; color: var(--body); }

  /* Graphics */
  .icon-block { position: absolute; top: 94px; width: 146px; }
  .icon-block--a { left: 52px; } .icon-block--b { left: 233px; } .icon-block--c { left: 420px; }
  .icon-block svg { display: block; margin: 0 auto; width: 46px; height: 46px; }
  .icon-block__title { margin-top: 16px; text-align: center; font-size: 11.5px; font-weight: 700; color: var(--orange); }
  .icon-block__body { margin-top: 6px; font-size: 7.4px; line-height: 12px; color: var(--body); text-align: justify; }

  /* Section & project */
  .deco-ring { position: absolute; border-radius: 50%; border: 1px solid rgba(255,255,255,0.22); }
  .hero-brand { position: absolute; display: flex; align-items: center; gap: 8px; }
  .hero-brand__dot { width: 34px; height: 34px; border-radius: 50%; background: var(--white); }
  .hero-brand__name { font-size: 34px; font-weight: 700; color: var(--white); letter-spacing: 0.5px; }
  .hero-title { position: absolute; font-size: 27px; font-weight: 800; color: var(--white); }
  .hero-body { position: absolute; color: var(--white); }
  .slide--section .hero-brand { left: 38px; top: 88px; }
  .slide--section .hero-title { left: 35px; top: 141px; }
  .slide--section .hero-body { left: 38px; top: 174px; width: 306px; font-size: 7.4px; line-height: 12.5px; font-weight: 600; }
  .slide--project .hero-brand { left: 35px; top: 124px; }
  .slide--project .hero-title { left: 35px; top: 160px; }
  .slide--project .hero-body { left: 36px; top: 194px; width: 276px; font-size: 9px; line-height: 12.2px; font-weight: 500; text-align: justify; }
  .backdrop { position: absolute; inset: 0; background: linear-gradient(120deg, #c07a3e 0%, #b4692b 45%, #a4602a 100%); }
  .backdrop-disc { position: absolute; left: 355px; top: 30px; width: 280px; height: 280px; border-radius: 50%; background: rgba(150,80,30,0.35); }
  .footer--plain { height: 13px; }

  /* Stats */
  .stats-ring { position: absolute; left: 174px; top: 74px; width: 184px; height: 184px; border-radius: 50%; border: 1px solid var(--orange-bright); }
  .photo--plans { left: 178px; top: 78px; width: 176px; height: 176px; background: radial-gradient(circle at 50% 40%, #e6c44a 0%, #9fb4d6 40%, #3c63a8 100%); }
  .stat { position: absolute; border-radius: 50%; color: var(--white); display: flex; flex-direction: column; align-items: center; justify-content: center; text-align: center; }
  .stat__value { font-size: 16px; font-weight: 500; line-height: 1; }
  .stat__label { font-size: 8px; font-weight: 500; margin-top: 2px; }
  .stat--staff { left: 297px; top: 62px; width: 58px; height: 58px; background: #3a3a3a; border: 2px solid var(--white); }
  .stat--projects { left: 144px; top: 206px; width: 80px; height: 80px; background: var(--orange); border: 2px solid var(--white); }
</style>
</head>
<body>

<section class="slide slide--one-col">
  <div class="top-rule"></div>
  <h2 class="slide-title">ONE <span>COL CONTENT</span></h2>
  <div class="brand"><span class="brand__dot"></span><span class="brand__name">HARBROOK</span></div>
  <h3 class="col-title">Col Title</h3>
  <div class="col-body">
    <p>Lorem Ipsum is simply dummy text of the printing and typesetting industry. Lorem Ipsum has been the industry's standard dummy text ever since the 1500s, when an unknown printer took a galley of type and scrambled it to make a type specimen book. It has survived not only five centuries, but also the leap into electronic typesetting, remaining essentially unchanged. Lorem Ipsum is simply dummy text of the printing and typesetting industry.</p>
    <p>Lorem Ipsum has been the industry's standard dummy text ever since the 1500s, when an unknown printer took a galley of type and scrambled it to make a type specimen book. It has survived not only five centuries, but also the leap into electronic typesetting, remaining essentially unchanged.</p>
  </div>
  <div class="frame-ring"></div>
  <div class="photo photo--workers" role="img" aria-label="Photo of two construction workers in hard hats and safety vests on a commercial site"></div>
  <span class="dot dot--orange" style="left:354px;top:87px;width:17px;height:17px;"></span>
  <span class="dot dot--grey" style="left:471px;top:237px;width:20px;height:20px;"></span>
  <div class="footer">Copyright @Text</div>
</section>

<section class="slide slide--three-col">
  <div class="top-rule top-rule--accent"></div>
  <h2 class="slide-title">3 <span>COL CONTENT</span></h2>
  <div class="brand"><span class="brand__dot"></span><span class="brand__name">HARBROOK</span></div>
  <span class="dot dot--orange" style="left:429px;top:44px;width:10px;height:10px;"></span>
  <div class="feature feature--a">
    <span class="photo photo--engineer" role="img" aria-label="Photo of a site engineer holding blueprints in front of a building under construction"></span>
    <h3 class="feature__title">Col Title Text here</h3>
    <p class="feature__body">Lorem Ipsum is simply dummy text of the printing and typesetting industry. Lorem Ipsum has been the industry's standard dummy text ever since the 1500s,</p>
  </div>
  <div class="feature feature--b">
    <span class="photo photo--engineer" role="img" aria-label="Photo of a site engineer holding blueprints in front of a building under construction"></span>
    <h3 class="feature__title">Col Title Text here</h3>
    <p class="feature__body">Lorem Ipsum is simply dummy text of the printing and typesetting industry. Lorem Ipsum has been the industry's standard dummy text ever since the 1500s,</p>
  </div>
  <div class="feature feature--c">
    <span class="photo photo--engineer" role="img" aria-label="Photo of a site engineer holding blueprints in front of a building under construction"></span>
    <h3 class="feature__title">Col Title Text here</h3>
    <p class="feature__body">Lorem Ipsum is simply dummy text of the printing and typesetting industry. Lorem Ipsum has been the industry's standard dummy text ever since the 1500s,</p>
  </div>
  <div class="footer">Copyright @Text</div>
</section>

<section class="slide slide--graphics">
  <div class="top-rule"></div>
  <h2 class="slide-title">OUR <span>GRAPHICS</span></h2>
  <div class="brand"><span class="brand__dot"></span><span class="brand__name">HARBROOK</span></div>
  <div class="icon-block icon-block--a">
    <svg viewBox="0 0 46 46" fill="none" stroke="#b4692b" stroke-width="1.6">
      <rect x="3" y="4" width="40" height="38" rx="2"/>
      <line x1="3" y1="12" x2="43" y2="12"/>
      <circle cx="8" cy="8" r="1.3"/><circle cx="12" cy="8" r="1.3"/><circle cx="16" cy="8" r="1.3"/>
      <line x1="8" y1="18" x2="30" y2="18"/><line x1="8" y1="24" x2="30" y2="24"/>
      <line x1="8" y1="30" x2="30" y2="30"/><line x1="8" y1="36" x2="30" y2="36"/>
      <line x1="34" y1="12" x2="34" y2="42"/>
      <circle cx="38.5" cy="22" r="1.8"/><circle cx="38.5" cy="30" r="1.8"/>
    </svg>
    <h3 class="icon-block__title">ICONS TITLE HERE</h3>
    <p class="icon-block__body">Lorem Ipsum is simply dummy text of the printing and typesetting industry. Lorem Ipsum has been the industry's standard dummy text ever since the 1500s, when an unknown printer took a galley of type and scrambled it to make a type specimen book. It has survived not only five centuries, but also the leap into electronic typesetting, remaining essentially</p>
  </div>
  <div class="icon-block icon-block--b">
    <svg viewBox="0 0 46 46" fill="none" stroke="#b4692b" stroke-width="1.6">
      <path d="M15 20 V12 a8 8 0 0 1 16 0 V20"/>
      <path d="M18.5 20 V12.5 a4.5 4.5 0 0 1 9 0 V20"/>
      <path d="M9 20 H37 V32 a14 12 0 0 1 -28 0 Z"/>
      <circle cx="23" cy="29" r="3"/>
      <path d="M21.5 31.5 L20.5 36 H25.5 L24.5 31.5"/>
    </svg>
    <h3 class="icon-block__title">ICONS TITLE HERE</h3>
    <p class="icon-block__body">Lorem Ipsum is simply dummy text of the printing and typesetting industry. Lorem Ipsum has been the industry's standard dummy text ever since the 1500s, when an unknown printer took a galley of type and scrambled it to make a type specimen book. It has survived not only five centuries, but also the leap into electronic typesetting, remaining essentially</p>
  </div>
  <div class="icon-block icon-block--c">
    <svg viewBox="0 0 46 46" fill="none" stroke="#b4692b" stroke-width="1.6">
      <rect x="2" y="4" width="42" height="26"/>
      <line x1="2" y1="33" x2="44" y2="33"/>
      <polyline points="7,24 13,17 18,21 25,13 30,18 38,10"/>
      <line x1="23" y1="33" x2="23" y2="38"/>
      <line x1="23" y1="36" x2="14" y2="44"/><line x1="23" y1="36" x2="32" y2="44"/>
    </svg>
    <h3 class="icon-block__title">ICONS TITLE HERE</h3>
    <p class="icon-block__body">Lorem Ipsum is simply dummy text of the printing and typesetting industry. Lorem Ipsum has been the industry's standard dummy text ever since the 1500s, when an unknown printer took a galley of type and scrambled it to make a type specimen book. It has survived not only five centuries, but also the leap into electronic typesetting, remaining essentially</p>
  </div>
  <div class="footer">Copyright @Text</div>
</section>

<section class="slide slide--section">
  <div class="deco-ring" style="left:320px;top:34px;width:420px;height:420px;"></div>
  <div class="deco-ring" style="left:-160px;top:-180px;width:420px;height:420px;"></div>
  <div class="hero-brand"><span class="hero-brand__dot"></span><span class="hero-brand__name">HARBROOK</span></div>
  <h2 class="hero-title">SECTION TITLE HERE</h2>
  <p class="hero-body">Lorem Ipsum is simply dummy text of the printing and typesetting industry. Lorem Ipsum has been the industry's standard dummy text ever since the 1500s.</p>
  <span class="dot" style="left:458px;top:298px;width:10px;height:10px;background:var(--orange-bright);"></span>
</section>

<section class="slide slide--project">
  <div class="backdrop" role="img" aria-label="Faint photo of construction blueprints and tools with an orange overlay"></div>
  <div class="backdrop-disc"></div>
  <div class="hero-brand"><span class="hero-brand__dot"></span><span class="hero-brand__name">HARBROOK</span></div>
  <h2 class="hero-title">PROJECT TITLE HERE</h2>
  <p class="hero-body">Lorem Ipsum is simply dummy text of the printing and typesetting industry. Lorem Ipsum has been the industry's standard dummy text ever since the 1500s.</p>
  <div class="footer footer--plain"></div>
</section>

<section class="slide slide--stats">
  <div class="top-rule top-rule--accent"></div>
  <h2 class="slide-title">OUR <span>STATICS</span></h2>
  <div class="brand"><span class="brand__dot"></span><span class="brand__name">HARBROOK</span></div>
  <div class="stats-ring"></div>
  <div class="photo photo--plans" role="img" aria-label="Photo of a yellow hard hat resting on blueprints with a folding ruler"></div>
  <div class="stat stat--staff"><span class="stat__value">100+</span><span class="stat__label">Staff</span></div>
  <div class="stat stat--projects"><span class="stat__value">1000+</span><span class="stat__label">Counstruction</span></div>
  <span class="dot dot--orange" style="left:429px;top:42px;width:10px;height:10px;"></span>
  <span class="dot dot--grey" style="left:457px;top:297px;width:10px;height:10px;"></span>
  <div class="footer">Copyright @Text</div>
</section>

</body>
</html>
```